Web Design for Rubbish Removal Company

I am looking for a custom web design that is clean and modern which also has a professional trustworthy feel to it.
The website is http://www.kendrawaste.com.au/ and need:
1 x Front Page
1 x Location Page
Please keep the green colour scheme as this is the corporate colours but would like to steer away from the black.
Industry/Entity Type
It Company
Number of Pages Required
2 page
Font styles to use
Sans Serif
Requirements
Must have
- Clean & Professional
- Keep green colour scheme
Should not have
- Steer away from black
- not look like a template

```html
<!DOCTYPE html>
<html lang="en">
<head>
<meta charset="utf-8">
<title>Kendra Waste – Rubbish Removal Sydney</title>
<link rel="stylesheet" href="https://fonts.googleapis.com/css2?family=Raleway:wght@400;500;600;700;800&family=Open+Sans:ital,wght@0,400;0,600;1,400&display=swap">
<style>
:root{
  --green:#7dc242;
  --green-dark:#5fa62c;
  --green-soft:#8ccc55;
  --ink:#3a3a3a;
  --muted:#666;
  --line:#e3e3e3;
  --paper:#ffffff;
  --mist:#f1f1f1;
  --orange:#f7a21b;
}
*{box-sizing:border-box;margin:0;padding:0}
html,body{width:1200px;height:3120px;overflow:hidden}
body{position:relative;background:var(--paper);font-family:"Open Sans",Arial,sans-serif;color:var(--ink)}
.abs{position:absolute}
.head-font{font-family:"Raleway",Arial,sans-serif}

/* header */
.brand{left:98px;top:48px;font-family:"Raleway",sans-serif;font-weight:800;font-size:32px;letter-spacing:-.5px;color:var(--ink);text-transform:uppercase}
.hotline{left:700px;top:44px;display:flex;gap:10px;align-items:center}
.hotline small{display:block;font-size:12px;color:var(--muted)}
.hotline strong{display:block;font-size:17px;font-weight:600;color:var(--ink)}
.book-btn{left:911px;top:44px;width:189px;height:36px;border:2px solid #555;border-radius:4px;font-size:13px;font-weight:600;display:flex;align-items:center;justify-content:center;color:var(--ink)}

/* nav */
.main-nav{left:0;top:125px;width:1200px;height:52px;background:var(--green);display:flex;padding-left:100px}
.main-nav a{color:#fff;text-decoration:none;font-family:"Raleway",sans-serif;font-weight:600;font-size:14px;text-transform:uppercase;height:52px;display:flex;align-items:center;padding:0 16px;margin-right:25px}
.main-nav a.active{background:var(--green-dark)}

/* hero */
.hero{left:0;top:177px;width:1200px;height:505px;background:linear-gradient(100deg,#8a5a48 0%,#a07866 30%,#d8d8d4 55%,#b3b0a8 75%,#555 100%)}
.hero-card{left:100px;top:339px;width:289px;height:216px;background:rgba(125,194,66,.92);padding:26px 24px;color:#fff}
.hero-card h2{font-family:"Raleway",sans-serif;font-size:20px;font-weight:700;text-transform:uppercase;padding-bottom:12px;border-bottom:1px solid rgba(255,255,255,.5);margin-bottom:12px}
.hero-card li{list-style:none;font-size:13px;font-weight:600;line-height:24px;text-transform:uppercase}
.slide-arrow{top:402px;width:34px;height:34px;border-radius:50%;background:rgba(0,0,0,.55);display:flex;align-items:center;justify-content:center}

/* welcome */
.welcome-title{left:0;top:733px;width:1200px;text-align:center;font-family:"Raleway",sans-serif;font-size:36px;font-weight:500}
.welcome-text{left:100px;top:786px;width:1000px;text-align:center;font-size:11.5px;line-height:19px;color:var(--muted)}
.services-title{left:0;top:870px;width:1200px;text-align:center;font-family:"Raleway",sans-serif;font-size:26px;font-weight:600}

.service-card{top:936px;width:314px;height:378px;background:#fff;box-shadow:0 2px 6px rgba(0,0,0,.14);text-align:center}
.service-card .photo{width:314px;height:180px}
.service-card .badge{position:absolute;left:0;top:158px;width:48px;height:42px;background:var(--green);display:flex;align-items:center;justify-content:center}
.service-card h3{margin-top:28px;font-family:"Raleway",sans-serif;font-weight:500;font-size:19px;line-height:24px;text-transform:uppercase}
.service-card p{margin:10px 26px 0;font-size:11.5px;line-height:19px;color:var(--muted)}
.more-btn{display:inline-flex;margin-top:12px;height:30px;padding:0 14px;background:var(--green);color:#fff;font-size:11px;font-weight:600;align-items:center;gap:6px}

/* band */
.band-photo{left:120px;top:1440px;width:480px;height:435px;background:radial-gradient(ellipse at 45% 65%,#d7b49a 0%,#c9c9c9 40%,rgba(255,255,255,0) 70%)}
.band-title{left:630px;top:1480px;color:#fff;font-family:"Raleway",sans-serif;font-weight:500;font-size:33px;line-height:38px;text-transform:uppercase}
.band-text{left:630px;top:1594px;width:460px;color:#fff;font-size:11.5px;line-height:19px}
.band-list{left:630px;top:1670px;list-style:none;color:#fff;font-size:11.5px}
.band-list li{height:20.5px;display:flex;align-items:center;gap:10px}

/* enquiry */
.enq-title{left:0;top:1970px;width:1200px;text-align:center;font-family:"Raleway",sans-serif;font-size:25px;font-weight:600}
.enq-text{left:250px;top:2012px;width:700px;text-align:center;font-size:13px;line-height:22px;color:var(--muted)}
.field{top:2104px}
.field label{display:block;font-size:12px;font-weight:600;margin-bottom:14px;text-transform:uppercase}
.field span{display:block;height:40px;border:1px solid var(--line)}
.send-btn{left:520px;top:2213px;width:158px;height:40px;background:var(--orange);color:#fff;font-size:13px;font-weight:600;display:flex;align-items:center;justify-content:center;border-radius:3px}

/* testimonials */
.testimonials{left:0;top:2350px;width:1200px;height:375px;background:var(--mist)}
.t-title{left:0;top:2418px;width:1200px;text-align:center;font-family:"Raleway",sans-serif;font-size:30px;font-weight:500}
.t-rule{left:565px;top:2468px;width:70px;height:3px;background:var(--green)}
.avatar{top:2523px;width:120px;height:120px;border-radius:50%;border:4px solid #fff;box-shadow:0 0 0 1px #ccc;background:linear-gradient(#c98f6b,#8b5a3d)}
.quote{top:2528px;width:380px;font-style:italic;font-size:12.5px;line-height:21px;color:var(--muted)}
.quote-name{top:2612px;font-style:italic;font-size:15px;line-height:22px;color:var(--ink)}
.quote-mark{top:2592px;font-family:Georgia,serif;font-size:90px;color:#bbb;line-height:1}

/* footer */
.footer-bg{left:0;top:2725px;width:1200px;height:343px;background:#f7f7f7}
.f-brand{left:98px;top:2808px;font-family:"Raleway",sans-serif;font-weight:800;font-size:25px;color:var(--ink);text-transform:uppercase}
.f-about{left:98px;top:2852px;width:260px;font-size:11.5px;line-height:19.5px;color:var(--muted)}
.f-head{top:2802px;font-family:"Raleway",sans-serif;font-size:17px;font-weight:600;text-transform:uppercase;letter-spacing:.5px}
.f-note{left:416px;top:2836px;width:250px;font-size:11.5px;line-height:19px;color:var(--muted)}
.f-input{left:416px;top:2885px;width:245px;height:42px;border:1px solid var(--line);background:#fff;font-size:11px;padding:0 12px;display:flex;align-items:center;color:var(--muted)}
.f-sub{left:416px;top:2937px;width:121px;height:31px;background:var(--green);color:#fff;font-size:11.5px;font-weight:600;display:flex;align-items:center;justify-content:center}
.contact-row{left:722px;display:flex;gap:12px;font-size:12.5px;line-height:19px;color:var(--muted)}
.socials{left:726px;top:2987px;display:flex;gap:6px}
.socials span{width:24px;height:24px;border:1px solid #666;border-radius:50%}
.links{left:995px;top:2830px;list-style:none;font-size:11.5px;line-height:22px;color:var(--muted)}
.copyright{left:0;top:3068px;width:1200px;height:52px;border-top:1px solid var(--line);background:#fff;text-align:center;font-size:11.5px;line-height:52px;color:var(--muted)}
</style>
</head>
<body>

<header>
  <div class="abs brand">Kendra Waste</div>
  <div class="abs hotline">
    <svg width="26" height="26" viewBox="0 0 24 24"><circle cx="12" cy="12" r="11" fill="none" stroke="#444" stroke-width="2"/><path d="M8 7c0 5 4 9 9 9l1-2-3-1-1 1c-2-1-3-2-4-4l1-1-1-3z" fill="#444"/></svg>
    <div><small>24/7 CUSTOMER SERVICE</small><strong>0400 555 018</strong></div>
  </div>
  <div class="abs book-btn">BOOK AN APPOINTMENT</div>
</header>

<nav class="abs main-nav">
  <a class="active">Home</a><a>About Us</a><a>Services</a><a>Gallery</a><a>FAQs</a><a>Testimonials</a><a>Locations</a><a>Contact Us</a>
</nav>

<section>
  <div class="abs hero" role="img" aria-label="Photo of a branded rubbish truck parked on a cobbled street beside brick buildings and bin bags"></div>
  <div class="abs hero-card">
    <h2>Kendra Waste</h2>
    <ul><li>Free Quote</li><li>Cheapest Price</li><li>Always On-Time</li><li>Same-Day</li><li>10+ Years Exp</li></ul>
  </div>
  <div class="abs slide-arrow" style="left:30px"><svg width="12" height="12" viewBox="0 0 12 12"><path d="M8 1 3 6l5 5" stroke="#fff" stroke-width="2" fill="none"/></svg></div>
  <div class="abs slide-arrow" style="left:1126px"><svg width="12" height="12" viewBox="0 0 12 12"><path d="M4 1l5 5-5 5" stroke="#fff" stroke-width="2" fill="none"/></svg></div>
</section>

<section>
  <h1 class="abs welcome-title">Welcome to Kendra Waste</h1>
  <p class="abs welcome-text">Kendra has been in the rubbish removal industry for over 10 years, working in excavation, strip outs, building site clean-ups and alongside many of the large waste operators in Australia. Kendra Waste is the result of a working life of experience and dedication to rubbish removal. Kendra's ability to handle removal work of all kinds is second to none, and a dedicated removal truck has let the business expand into collection and recycling.</p>
  <h2 class="abs services-title">Sydney's Cheapest Rubbish Removal Services</h2>

  <article class="abs service-card" style="left:98px">
    <div class="photo" role="img" aria-label="Photo of household junk and furniture piled on a footpath" style="background:linear-gradient(135deg,#6f8a4a,#a79a86 60%,#5d6d80)"></div>
    <div class="badge"><svg width="18" height="16" viewBox="0 0 18 16"><path d="M9 1 1 8h2v7h4v-5h4v5h4V8h2z" fill="#fff"/></svg></div>
    <h3>Household Rubbish<br>Removals</h3>
    <p>Do you have rubbish slowly building up at home? Quickly running out of space or simply letting household junk pile up? Kendra Waste</p>
    <span class="more-btn">FIND OUT MORE ⊕</span>
  </article>
  <article class="abs service-card" style="left:443px">
    <div class="photo" role="img" aria-label="Photo of stacked office chairs and furniture ready for removal" style="background:linear-gradient(135deg,#7a4d45,#9a8f8a 55%,#5a5552)"></div>
    <div class="badge"><svg width="18" height="14" viewBox="0 0 18 14"><path d="M1 2h6l2 2h8v9H1z" fill="#fff"/></svg></div>
    <h3>Office Rubbish<br>Removals</h3>
    <p>Most companies are often busy improving business practices and taking care of customers to notice that office rubbish and junk can slowly build</p>
    <span class="more-btn">FIND OUT MORE ⊕</span>
  </article>
  <article class="abs service-card" style="left:788px">
    <div class="photo" role="img" aria-label="Photo of timber and construction debris in a building site" style="background:linear-gradient(135deg,#8a6a45,#b08a5e 55%,#6a5540)"></div>
    <div class="badge"><svg width="14" height="16" viewBox="0 0 14 16"><path d="M1 3h12M5 3V1h4v2M2 3l1 12h8l1-12" stroke="#fff" stroke-width="2" fill="none"/></svg></div>
    <h3>Construction Rubbish<br>Removals</h3>
    <p>Construction and demolition materials usually consist of heavy bricks, timber, concrete, rubble, steel and plastics. These materials are often left</p>
    <span class="more-btn">FIND OUT MORE ⊕</span>
  </article>
</section>

<section>
  <svg class="abs" style="left:0;top:1398px" width="1200" height="500" viewBox="0 0 1200 500">
    <defs><linearGradient id="bandGrad" x1="0" x2="1"><stop offset="0" stop-color="#79bf44"/><stop offset="1" stop-color="#6fb63a"/></linearGradient></defs>
    <polygon points="0,24 710,24 740,0 1200,0 1200,474 470,474 440,499 0,499" fill="url(#bandGrad)"/>
  </svg>
  <div class="abs band-photo" role="img" aria-label="Photo of a smiling worker giving a thumbs up in front of a branded tipper truck"></div>
  <h2 class="abs band-title">Best Ever Services<br>Maintenance</h2>
  <p class="abs band-text">Kendra Waste offers complete rubbish removal services for your home or business including residential households, offices, retail locations, building sites, demolition and more. We are a trusted Sydney rubbish removal company.</p>
  <ul class="abs band-list">
    <li><svg width="11" height="9" viewBox="0 0 11 9"><path d="M1 4l3 3 6-6" stroke="#fff" stroke-width="2" fill="none"/></svg>Complete rubbish clean-out, including demolition, strip outs and labour hire</li>
    <li><svg width="11" height="9" viewBox="0 0 11 9"><path d="M1 4l3 3 6-6" stroke="#fff" stroke-width="2" fill="none"/></svg>Removal of white goods, garden rubbish, furniture and more</li>
    <li><svg width="11" height="9" viewBox="0 0 11 9"><path d="M1 4l3 3 6-6" stroke="#fff" stroke-width="2" fill="none"/></svg>No job is too large, too small or too difficult</li>
    <li><svg width="11" height="9" viewBox="0 0 11 9"><path d="M1 4l3 3 6-6" stroke="#fff" stroke-width="2" fill="none"/></svg>Extra discounts for returning customers</li>
    <li><svg width="11" height="9" viewBox="0 0 11 9"><path d="M1 4l3 3 6-6" stroke="#fff" stroke-width="2" fill="none"/></svg>Free quote provided with all enquiries</li>
    <li><svg width="11" height="9" viewBox="0 0 11 9"><path d="M1 4l3 3 6-6" stroke="#fff" stroke-width="2" fill="none"/></svg>Over 10 years in the rubbish removal trade</li>
    <li><svg width="11" height="9" viewBox="0 0 11 9"><path d="M1 4l3 3 6-6" stroke="#fff" stroke-width="2" fill="none"/></svg>Same-day rubbish and waste collection</li>
    <li><svg width="11" height="9" viewBox="0 0 11 9"><path d="M1 4l3 3 6-6" stroke="#fff" stroke-width="2" fill="none"/></svg>CHEAPEST PRICES in Sydney</li>
  </ul>
</section>

<section>
  <h2 class="abs enq-title">ENQUIRE NOW AND RECEIVE A CALL BACK WITHIN 60 MINUTES!</h2>
  <p class="abs enq-text">Kendra Waste offers some of the best prices in Sydney. We provide an unrivalled, friendly and affordable, same-day rubbish clean-out to all suburbs in Sydney.</p>
  <div class="abs field" style="left:133px;width:241px"><label>Name *</label><span></span></div>
  <div class="abs field" style="left:389px;width:214px"><label>Email *</label><span></span></div>
  <div class="abs field" style="left:620px;width:216px"><label>Phone</label><span></span></div>
  <div class="abs field" style="left:851px;width:216px"><label>Message</label><span></span></div>
  <div class="abs send-btn">SEND ENQUIRY</div>
</section>

<section>
  <div class="abs testimonials"></div>
  <h2 class="abs t-title">TESTIMONIALS</h2>
  <div class="abs t-rule"></div>

  <div class="abs avatar" style="left:98px" role="img" aria-label="Portrait photo of a customer"></div>
  <p class="abs quote" style="left:240px">" Quick, tidy and friendly crew who cleared our whole garage in under an hour. Fair price, no mess left behind, and they even swept up after."</p>
  <p class="abs quote-name" style="left:240px">Mara Quinn -<br>Kendra Waste</p>
  <div class="abs quote-mark" style="left:530px">”</div>

  <div class="abs avatar" style="left:637px" role="img" aria-label="Portrait photo of a customer"></div>
  <p class="abs quote" style="left:779px">" Booked in the morning and the truck arrived the same afternoon. The team was polite, careful and the final price matched the quote exactly."</p>
  <p class="abs quote-name" style="left:779px">Tobias Reed -<br>Kendra Waste</p>
  <div class="abs quote-mark" style="left:1058px">”</div>
</section>

<footer>
  <div class="abs footer-bg"></div>
  <div class="abs f-brand">Kendra Waste</div>
  <p class="abs f-about">Kendra has been in the rubbish removal industry for over 10 years. We specialise in residential rubbish removals, deceased estate clean-ups, building site rubbish removal and have worked with many large rubbish removal organisations in Australia. If you have rubbish that needs disposing, Kendra can help. Call us for a free quote today.</p>

  <h4 class="abs f-head" style="left:416px">Sign Up For Newsletter</h4>
  <p class="abs f-note">Get our latest news, seasonal offers and handy clean-up tips sent to you.</p>
  <div class="abs f-input">Enter email</div>
  <div class="abs f-sub">SUBSCRIPTION</div>

  <h4 class="abs f-head" style="left:722px">Contact Us</h4>
  <div class="abs contact-row" style="top:2840px"><svg width="12" height="16" viewBox="0 0 12 16"><path d="M6 0a6 6 0 0 0-6 6c0 4 6 10 6 10s6-6 6-10a6 6 0 0 0-6-6zm0 8a2 2 0 1 1 0-4 2 2 0 0 1 0 4z" fill="#555"/></svg><span>Kendra Waste<br>48 Harbour Lane, Marrick,<br>NSW 2204</span></div>
  <div class="abs contact-row" style="top:2912px"><svg width="14" height="14" viewBox="0 0 24 24"><path d="M5 2c0 9 8 17 17 17l1-4-5-2-2 2c-3-1-6-4-7-7l2-2-2-5z" fill="#555"/></svg><span>Phone:&nbsp; 0400 555 018</span></div>
  <div class="abs contact-row" style="top:2944px"><svg width="14" height="12" viewBox="0 0 14 12"><path d="M0 0h14v12H0zM0 1l7 5 7-5" fill="#555" stroke="#f7f7f7" stroke-width="1"/></svg><span>hello@kendrawaste.com.au</span></div>
  <div class="abs socials"><span></span><span></span><span></span><span></span></div>

  <h4 class="abs f-head" style="left:995px">Quick Links</h4>
  <ul class="abs links"><li>Home</li><li>About</li><li>Services</li><li>Gallery</li><li>Faqs</li><li>Testimonials</li><li>Locations</li><li>Blog</li></ul>

  <div class="abs copyright">©2015 - 2016 Kendra Waste. All Rights Reserved.</div>
</footer>

</body>
</html>
```